Flyer-Design für Keramik Verdunster
Zielgruppe
Wir wollen Keramik Verdunster bei Volkarn Verkaufen und dieser Flyer soll in jede Produktverpackung mit hinein gelegt werden.
Aufgabenstellung
Der Flyer sollte möglichst klein gehalten werden, also mehrmals Faltbar. Kann auf Vorder- und Rückseite bedruckt werden.
Ihrer Kreativität sind von unserer seite aus ,keine Grenzen gesetzt.
Im Anhang unser Logo , was mit auf den Flyer muss und in der Worddatei haben wir in Klammern noch Instruktionen für sie mit reingeschrieben. Design ect. ist Ihnen überlassen

```html
<!DOCTYPE html>
<html lang="de">
<head>
<meta charset="utf-8">
<title>Lunavio Faltblatt – Anleitung für ein ideales Raumklima</title>
<link href="https://fonts.googleapis.com/css2?family=Asap:wght@400;500;600;700&family=M+PLUS+Rounded+1c:wght@400;500&display=swap" rel="stylesheet">
<style>
:root{
  --bg:#cfcfd1;
  --bg-light:#e4e4e6;
  --paper:#ffffff;
  --purple:#4a1f8c;
  --navy:#22295e;
  --blue:#2a82c8;
  --sky:#a9cbeb;
  --sky-soft:#cfe1f3;
  --ink:#3a3a3f;
  --grey:#5c5c62;
  --photo-a:#c9bfe6;
  --photo-b:#f1ddd2;
}
*{box-sizing:border-box;margin:0;padding:0}
html,body{width:1200px;height:2626px;overflow:hidden}
body{background:radial-gradient(ellipse at 50% 30%,var(--bg-light),var(--bg) 70%);font-family:"Asap",sans-serif;color:var(--ink);position:relative}
.abs{position:absolute}
.panel{position:absolute;background:var(--paper);box-shadow:0 6px 18px rgba(0,0,0,.18);overflow:hidden}
.photo{position:absolute;background:linear-gradient(120deg,var(--photo-a) 0%,#ddd6ee 45%,var(--photo-b) 75%,#f7f3f0 100%)}
.brand{display:flex;align-items:center;gap:10px;color:var(--purple);font-weight:700;letter-spacing:.18em}
.brand .dot{border-radius:50%;background:var(--purple)}
.band{position:absolute;background:var(--purple);color:#fff;font-weight:500;letter-spacing:.14em;text-align:right}
.title{position:absolute;font-weight:700;color:var(--grey);line-height:1.05}

/* banner */
.banner{position:absolute;left:0;top:897px;width:1200px;height:134px;background:var(--blue);color:#fff;font-family:"M PLUS Rounded 1c",sans-serif;padding:12px 0 0 78px}
.banner .big{font-size:58px;font-weight:500}
.banner .rest{font-size:38px}
.banner .sub{font-size:38px;margin-top:-6px}
.caption{position:absolute;width:1200px;text-align:center;font-family:"M PLUS Rounded 1c",sans-serif;font-size:38px;color:#222}

/* outside spread */
.knowhow h2{font-size:18px;color:var(--navy);font-weight:700;margin-bottom:10px}
.knowhow h2 span{color:var(--blue)}
.knowhow p{font-size:12.5px;line-height:1.35;color:var(--grey)}
.knowhow p.strong{font-weight:700;color:var(--ink);margin-top:6px}
.knowhow h3{text-align:center;color:var(--blue);font-size:17px;margin:24px 0 8px}
.knowhow .note{text-align:center}

/* inside spread */
.steps h2{font-size:14.5px;color:var(--navy);font-weight:700;line-height:1.15;margin-bottom:10px}
.step{display:flex;gap:8px;margin-bottom:12px;font-size:10.5px;line-height:1.3;color:var(--grey)}
.step b{color:var(--ink)}
.num{flex:0 0 18px;height:18px;border-radius:50%;background:var(--blue);color:#fff;font-size:10px;font-weight:700;display:flex;align-items:center;justify-content:center}
.col h2{font-size:13px;color:var(--blue);font-weight:600;line-height:1.2;margin-bottom:8px}
.col p{font-size:10px;line-height:1.3;color:var(--grey);margin-bottom:6px}
.col p.strong{font-weight:700;color:var(--ink)}
.climate{display:grid;grid-template-columns:105px 110px 100px;gap:0 12px;margin-top:10px}
.climate .head{font-size:11px;color:var(--navy);height:40px}
.climate .head.tag{background:var(--sky);color:#fff;padding:4px 8px;height:22px}
.climate .cells{background:var(--sky-soft);color:#fff;font-size:10px;line-height:1.3;padding:8px;height:108px;background:linear-gradient(var(--sky),var(--sky-soft))}
.climate .cells.c{text-align:center}
.small{font-size:7px!important;margin-top:12px}
.months{width:100%;border-collapse:collapse;font-size:10px;margin:6px 0}
.months th{background:var(--blue);color:#fff;font-weight:600;text-align:left;padding:2px 5px}
.months tr.alt th{background:var(--sky)}
.months td{padding:5px;color:var(--navy)}
</style>
</head>
<body>

<!-- folded cover, shown flat -->
<section class="panel" style="left:320px;top:120px;width:620px;height:620px">
  <div class="photo" role="img" aria-label="Foto: schlafendes Baby mit lila Strickmütze" style="left:0;top:0;width:620px;height:350px"></div>
  <div class="abs" style="left:0;top:350px;width:620px;height:270px;background:linear-gradient(#f6f6f8,#eaf1f6)"></div>
  <div class="title" style="left:40px;top:420px;font-size:40px">Anleitung für ein<br>ideales Raumklima</div>
  <div class="abs brand" style="left:470px;top:390px;font-size:22px"><span class="dot" style="width:40px;height:40px"></span></div>
  <div class="band" style="left:30px;top:530px;width:590px;height:36px;font-size:20px;padding:6px 20px">LUNAVIO</div>
</section>

<div class="banner">
  <div><span class="big">faltblatt</span> <span class="rest">gefalzt auf quadrat 10.0 cm x 10.0 cm</span></div>
  <div class="sub">6-seiter (wickelfalz)</div>
</div>

<!-- outside spread -->
<section class="panel knowhow" style="left:22px;top:1120px;width:400px;height:440px;padding:36px 30px 0 48px">
  <h2>Wissenswertes <span>zur</span> Luftfeuchtigkeit</h2>
  <p>Das gesündeste Raumklima herrscht bei 50 % relativer Luftfeuchte und 20 °C Raumtemperatur.</p>
  <p>Die relative Raumfeuchte sollte nicht unter 30 % fallen. Einige Schimmelpilzarten vermehren sich bereits ab 70 % Feuchtigkeit.</p>
  <p class="strong">Herrschen über einen längeren Zeitraum mehr als 80 % Feuchtigkeit im Raum, führt das unvermeidlich zur Entstehung von Schimmel.</p>
  <h3>Merke !</h3>
  <p class="note">Die Verdunstungsdauer hängt von den verschiedensten Faktoren ab. Je gesättigter Ihre rel. Luftfeuchtigkeit im Raum (durch schlechtes Lüften) und je kälter der Heizkörper desto länger dauert der Verdunstungsprozess!</p>
  <p class="note strong">Die Luft kann dadurch nicht mehr Feuchtigkeit aufnehmen!</p>
</section>
<section class="panel" style="left:422px;top:1120px;width:372px;height:440px;background:linear-gradient(#e2e2e4,#f4f4f6)">
  <div class="abs brand" style="left:0;top:190px;width:372px;justify-content:center;font-size:26px"><span class="dot" style="width:22px;height:22px"></span>LUNAVIO</div>
</section>
<section class="panel" style="left:794px;top:1120px;width:388px;height:440px">
  <div class="photo" role="img" aria-label="Foto: schlafendes Baby mit lila Strickmütze" style="left:18px;top:30px;width:370px;height:250px"></div>
  <div class="abs" style="left:18px;top:280px;width:370px;height:160px;background:linear-gradient(#f4f4f6,#eef3f7)"></div>
  <div class="title" style="left:44px;top:305px;font-size:24px">Anleitung für ein<br>ideales Raumklima</div>
  <div class="abs brand" style="left:315px;top:300px"><span class="dot" style="width:50px;height:50px"></span></div>
  <div class="band" style="left:22px;top:380px;width:366px;height:24px;font-size:15px;padding:3px 28px">LUNAVIO</div>
</section>
<div class="caption" style="top:1590px">Flyer Außen geöffnet</div>

<!-- inside spread -->
<section class="panel steps" style="left:26px;top:2010px;width:390px;height:420px;padding:48px 20px 0 60px">
  <h2>Was muss ich beachten und wie funktionieren meine neuen Lunavio Heizkörper Luftbefeuchter.</h2>
  <div class="step"><span class="num">1.</span><span>Füllen Sie Ihre neuen Luftbefeuchter mit warmen Wasser, idealerweise mit entkalktem Wasser.</span></div>
  <div class="step"><span class="num">2.</span><span><b>Sollten Sie kein entkalktes Wasser haben, sollten Sie Ihre Verdunster nach jedem Durchgang (Komplett verdunstet) mit verdünntem Essig oder Zitronensäure von Innen reinigen, um die Poren Kalk frei zu halten und um eine optimale Verdunstung zu gewährleisten.</b></span></div>
  <div class="step"><span class="num">3.</span><span>Um weiterhin eine optimale Verdunstung zu gewährleisten, sollte Ihr Heizkörper so warm sein, dass Sie ihn gerade noch mit der Hand anfassen können oder noch heißer.</span></div>
  <div class="step"><span class="num">4.</span><span><b>Bringen Sie an jedem Heizkörper zwei Verdunster an. Außer im Bad und der Küche!</b></span></div>
  <div class="step"><span class="num">5.</span><span>Wenn die Verdunster zu lange an einem Heizkörper hängen, die abgeschaltet bzw. kalt sind, dann kann es zur Tröpfchenbildung kommen, weil die Poren groß sind und bei kalter Oberfläche kann das Wasser nicht schnell genug verdunsten.</span></div>
</section>
<section class="panel col" style="left:416px;top:2010px;width:372px;height:420px;padding:50px 14px 0 14px">
  <h2>Was muss ich beachten und wie funktionieren meine neuen Lunavio Heizkörper Luftbefeuchter.</h2>
  <p class="strong">Für ein schönes Klima sorgen Sie, wie folgt:</p>
  <p>relative Luftfeuchtigkeit in Wohnräumen<br>In der folgenden Tabelle finden Sie die optimalen Werte für relative Luftfeuchte und Temperatur in den verschiedenen Wohnbereichen.</p>
  <p class="strong">Als ideale Mittelwerte haben sich 40 - 60 % Feuchte und 20 °C Raumtemperatur bewährt.</p>
  <div class="climate">
    <div class="head"><div class="tag head" style="height:22px;background:var(--sky);color:#fff;padding:3px 6px">IDEALES RAUMKLIMA</div>Raum</div>
    <div class="head">Optimale<br>Temperatur</div>
    <div class="head">Optimale<br>Luftfeuchtigkeit</div>
    <div class="cells">Wohnräume<br>Schlafzimmer<br>Kinderzimmer<br>Küche<br>Badezimmer<br>Keller</div>
    <div class="cells c">20 °C<br>16 - 18 °C<br>20 - 22 °C<br>18 °C<br>23 °C<br>10 - 15 °C</div>
    <div class="cells c">40 - 60 %<br>40 - 60 %<br>40 - 60 %<br>50 - 60 %<br>50 - 70 %<br>50 - 65 %</div>
  </div>
  <p class="small strong">In Küche und Bad liegt die Luftfeuchte naturgemäß etwas höher und kann beim Kochen oder Duschen kurz über diese Werte steigen. Das ist unbedenklich, wenn Sie danach den Wasserdampf sofort nach draußen lüften.</p>
</section>
<section class="panel col" style="left:788px;top:2010px;width:374px;height:420px;padding:40px 18px 0 14px">
  <h2>Richtiges Lüften</h2>
  <p>Schließen Sie den Thermostat kopf der Heizungen komplett. Öffnen Sie die Fenster zweier gegenüberliegender Räume gleichzeitig und lassen auch die Türen offen stehen. Auf diese Weise entsteht ein Durchzug und die warme, verbrauchte Luft zieht schneller nach draußen ab.</p>
  <p class="strong">Achtung: Vergessen Sie nicht, auch im zweiten Raum, den Heizkörper während des Lüftens abzustellen!</p>
  <h2>Wie oft sollten Sie Lüften?</h2>
  <p>Optimal wäre 4 mal am Tag, da dies aber oft nicht möglich ist, sollten Sie mindestens 2 mal am Tag Lüften, abends vor dem schlafen gehen und morgens nach dem aufstehen.</p>
  <p class="strong" style="color:var(--navy)">Dauer des Lüftens:</p>
  <table class="months">
    <tr><th>Januar</th><th>Februar</th><th>März</th><th>April</th><th>Mai</th><th>Juni</th><th>Juli</th></tr>
    <tr><td>5 min.</td><td>5 min.</td><td>10 min.</td><td>15 min.</td><td>20 min.</td><td>30 min.</td><td>30 min.</td></tr>
    <tr class="alt"><th>August</th><th>September</th><th>Oktober</th><th>November</th><th colspan="3">Dezember</th></tr>
    <tr><td>30 min.</td><td>15 min.</td><td>20 min.</td><td>10 min.</td><td colspan="3">5 min.</td></tr>
  </table>
  <p>Wenn Sie nun so vorgehen wie beschrieben, wird Ihnen und dem wunderbaren Gefühl eines schönen Klimas im Zuhause, nichts mehr im Wege stehen.</p>
</section>
<div class="caption" style="top:2470px">Flyer Innen geöffnet</div>

</body>
</html>
```